Startup needs a Powerpoint presentation for investors

We are raising capital and we need to show the project to new investors. Our website is: plumfarow.es.

We need the presentation to be modified by us with new numbers, text, etc.

We need to redesign everything: chats, font (we like Lato, but we are open to suggestions), etc.

We are open to new ideas, but we have preference for Lato font and our color palette. We like clean presentations (white backgrounds) and we use color or emojis to highlight things.

You can see how we design entering our app: app.plumfarow.es
Updates

To win the contest you do not need to design every slide. You can choose to design some of them for us to see how it would be and after you win you can design the others.

Industry/Entity Type

Startup

Font styles to use
Other font styles liked:
• Lato

Requirements
Must have
• Editable for us.
Nice to have
• Use our color palette (you can use more colors if you like):
• Black: #575756
• Grey 1: #B9B9B9
• Grey 2: #575756 (A = 15)
• Grey 3: #F9F9F9
• White: #FFFFFF
• Green 1: #197A45
• Green 2: #197A45 (A = 11)

```html
<!DOCTYPE html>
<html lang="en">
<head>
<meta charset="utf-8">
<title>Plumfarow — Investor Deck</title>
<link rel="stylesheet" href="https://fonts.googleapis.com/css2?family=Lato:wght@400;700&display=swap">
<style>
  :root {
    --stage: #252122;
    --bar: #060608;
    --white: #ffffff;
    --black: #575756;
    --grey-1: #b9b9b9;
    --grey-3: #f9f9f9;
    --green-1: #197a45;
    --green-band: rgba(25, 122, 69, 0.68);
    --green-tint: rgba(25, 122, 69, 0.11);
    --text-soft: #6b6b6a;
  }
  * { box-sizing: border-box; margin: 0; padding: 0; }
  html, body {
    width: 849px; height: 1200px; overflow: hidden;
    background: var(--stage);
    font-family: "Lato", Arial, sans-serif;
  }
  .canvas { position: relative; width: 849px; height: 1200px; }
  .slide { position: absolute; background: var(--bar); }
  .slide__page { position: absolute; left: 0; right: 0; background: var(--white); overflow: hidden; }

  /* Cover */
  .slide--cover { left: 152px; top: 13px; width: 555px; height: 363px; }
  .slide--cover .slide__page { top: 52px; height: 311px; }
  .cover__photo {
    position: absolute; left: 140px; top: 0; right: 0; bottom: 0;
    background:
      radial-gradient(ellipse 60% 70% at 55% 40%, rgba(205,170,150,0.55), rgba(205,170,150,0) 70%),
      linear-gradient(90deg, rgba(255,255,255,1) 0%, rgba(226,218,214,0.6) 35%, rgba(190,180,178,0.55) 70%, rgba(240,238,240,0.8) 100%);
  }
  .brand { position: absolute; left: 28px; top: 121px; display: flex; align-items: center; gap: 12px; }
  .brand__dot { width: 40px; height: 40px; border-radius: 50%; background: var(--green-1); }
  .brand__name { font-size: 26px; font-weight: 700; color: var(--black); letter-spacing: -0.2px; }
  .cover__band {
    position: absolute; left: 0; right: 0; top: 178px; height: 55px;
    background: var(--green-band);
    display: flex; align-items: center; padding-left: 25px;
  }
  .cover__tagline { color: var(--white); font-size: 21px; font-weight: 400; }

  /* Section */
  .slide--section { left: 149px; top: 390px; width: 558px; height: 365px; }
  .slide--section .slide__page { top: 52px; height: 313px; }
  .section__decor {
    position: absolute; left: 345px; top: -40px; width: 270px; height: 270px;
    border-radius: 50%; background: var(--green-tint);
  }
  .section__title {
    position: absolute; left: 37px; top: 140px;
    display: flex; align-items: center; gap: 6px;
    font-size: 32px; color: var(--text-soft); font-weight: 400;
  }
  .section__bullet { width: 15px; height: 15px; border-radius: 50%; background: var(--green-1); }
  .section__lead { position: absolute; left: 67px; top: 180px; font-size: 14px; color: var(--text-soft); }

  /* Process */
  .slide--process { left: 143px; top: 757px; width: 573px; height: 430px; }
  .slide--process .slide__page { top: 54px; height: 322px; }
  .process__svg { position: absolute; left: 0; top: 0; }
  .process__heading {
    position: absolute; left: 63px; top: 32px;
    font-size: 13px; font-weight: 700; color: var(--green-1);
  }
  .process__label {
    position: absolute; width: 130px; text-align: center;
    font-size: 10.5px; line-height: 14px; color: var(--text-soft);
  }
</style>
</head>
<body>
<main class="canvas">

  <section class="slide slide--cover">
    <div class="slide__page">
      <div class="cover__photo" role="img" aria-label="Group of friends smiling while looking at a phone together"></div>
      <div class="brand">
        <span class="brand__dot"></span>
        <span class="brand__name">Plumfarow</span>
      </div>
      <div class="cover__band"><p class="cover__tagline">Play lottery with your friends</p></div>
    </div>
  </section>

  <section class="slide slide--section">
    <div class="slide__page">
      <div class="section__decor"></div>
      <h2 class="section__title"><span class="section__bullet"></span>Problem</h2>
      <p class="section__lead">Playing lottery in group is a nightmare 😱</p>
    </div>
  </section>

  <section class="slide slide--process">
    <div class="slide__page">
      <svg class="process__svg" width="573" height="322" viewBox="0 0 573 322">
        <circle cx="24" cy="24" r="20" fill="#b9b9b9" opacity="0.6"/>
        <circle cx="49" cy="46" r="6" fill="var(--green-1)"/>

        <!-- step 1 -->
        <path d="M87 92 a40 40 0 1 0 0 -1 Z" fill="none"/>
        <g>
          <path d="M47 133 a40 40 0 0 1 68 -28 L139 133 L115 161 a40 40 0 0 1 -68 -28 Z" fill="var(--green-1)"/>
          <rect x="72" y="120" width="26" height="16" rx="2" fill="none" stroke="#fff" stroke-width="2"/>
          <circle cx="85" cy="128" r="4" fill="#fff"/>
          <path d="M68 146 h30" stroke="#fff" stroke-width="3" stroke-linecap="round"/>
          <circle cx="57" cy="100" r="16" fill="#b9b9b9"/>
          <text x="57" y="104" font-size="9" fill="#444" text-anchor="middle" font-family="Lato, sans-serif">01</text>
          <path d="M87 174 v26" stroke="#777" stroke-dasharray="2 2"/>
          <path d="M84 198 l3 4 l3 -4" fill="none" stroke="#777"/>
        </g>
        <!-- step 2 -->
        <g>
          <path d="M172 133 a40 40 0 0 1 68 -28 L264 133 L240 161 a40 40 0 0 1 -68 -28 Z" fill="var(--black)"/>
          <rect x="193" y="125" width="38" height="16" rx="2" fill="none" stroke="#fff" stroke-width="1.5"/>
          <text x="212" y="136" font-size="8" fill="#fff" text-anchor="middle" font-family="Lato, sans-serif">TICKET</text>
          <circle cx="183" cy="96" r="16" fill="#b9b9b9"/>
          <text x="183" y="100" font-size="9" fill="#444" text-anchor="middle" font-family="Lato, sans-serif">02</text>
          <path d="M212 174 v26" stroke="#777" stroke-dasharray="2 2"/>
          <path d="M209 198 l3 4 l3 -4" fill="none" stroke="#777"/>
        </g>
        <!-- step 3 -->
        <g>
          <path d="M302 133 a40 40 0 0 1 68 -28 L394 133 L370 161 a40 40 0 0 1 -68 -28 Z" fill="var(--green-1)"/>
          <rect x="343" y="115" width="16" height="28" rx="3" fill="none" stroke="#fff" stroke-width="2"/>
          <rect x="322" y="133" width="18" height="10" rx="2" fill="none" stroke="#fff" stroke-width="1.5"/>
          <path d="M328 126 a12 12 0 0 1 14 -10" fill="none" stroke="#fff" stroke-width="1.5"/>
          <circle cx="313" cy="94" r="16" fill="#b9b9b9"/>
          <text x="313" y="98" font-size="9" fill="#444" text-anchor="middle" font-family="Lato, sans-serif">03</text>
          <path d="M342 174 v26" stroke="#777" stroke-dasharray="2 2"/>
          <path d="M339 198 l3 4 l3 -4" fill="none" stroke="#777"/>
        </g>
        <!-- step 4 -->
        <g>
          <path d="M435 133 a40 40 0 0 1 68 -28 L527 133 L503 161 a40 40 0 0 1 -68 -28 Z" fill="var(--black)"/>
          <path d="M462 146 L480 118 L492 146 Z" fill="none" stroke="#fff" stroke-width="2"/>
          <path d="M480 118 v-8 l8 3 l-8 3" fill="#fff" stroke="#fff" stroke-width="1"/>
          <circle cx="445" cy="96" r="16" fill="#b9b9b9"/>
          <text x="445" y="100" font-size="9" fill="#444" text-anchor="middle" font-family="Lato, sans-serif">04</text>
          <path d="M475 174 v26" stroke="#777" stroke-dasharray="2 2"/>
          <path d="M472 198 l3 4 l3 -4" fill="none" stroke="#777"/>
        </g>

        <path d="M33 290 H297" stroke="var(--green-1)" stroke-width="2"/>
        <path d="M297 290 H559" stroke="#b9b9b9" stroke-width="1.5"/>
      </svg>
      <h3 class="process__heading">Plumfarow was created to solve a pain we had: play lottery with our friends</h3>
      <p class="process__label" style="left:22px; top:218px;">Gather everyone’s<br>money</p>
      <p class="process__label" style="left:147px; top:218px;">Purchase the<br>lottery ticket</p>
      <p class="process__label" style="left:277px; top:218px;">Send a copy of the<br>ticket</p>
      <p class="process__label" style="left:410px; top:218px;">Hope that your friend is<br>not in the caribbean<br>with your money</p>
    </div>
  </section>

</main>
</body>
</html>
```